body balm label design

body balm tube design, current label design for other similar products
Need to have a design which can interchange between 3 different solutions
Amber Tide (Lavender + Vanilla)
Copper Harbor (Eucalyptus + Mint)
Velvet Arc (Bergamot + Cedarwood)
Tube size:
2.5h x 3.25 w
Target Market(s)
natural, solution focused
Requirements
Must have
- relatable to existing brand designs, focus on features and benefits

```html
<!DOCTYPE html>
<html lang="en">
<head>
<meta charset="utf-8">
<title>Body Balm Label Set</title>
<link rel="stylesheet" href="https://fonts.googleapis.com/css2?family=Playfair+Display:wght@800&family=Nunito+Sans:wght@400;600&display=swap">
<style>
  :root {
    --canvas: #f4efe8;
    --sleep-bg: #e6e2f7;
    --sleep-ink: #3a33a8;
    --sleep-art: #c9c2ef;
    --stress-bg: #fbd9c4;
    --stress-ink: #7a3418;
    --stress-art: #efb898;
    --muscle-bg: #e6f3e0;
    --muscle-ink: #2f5c4a;
    --muscle-art: #c3dfc0;
  }
  * { box-sizing: border-box; margin: 0; padding: 0; }
  html, body { width: 1200px; height: 800px; overflow: hidden; }
  body {
    background: var(--canvas);
    font-family: "Nunito Sans", sans-serif;
    display: flex;
    align-items: center;
    justify-content: center;
    gap: 48px;
  }
  .label {
    width: 320px;
    height: 560px;
    background: var(--bg);
    color: var(--ink);
    border-radius: 6px;
    display: flex;
    flex-direction: column;
    align-items: center;
    padding-top: 64px;
    text-align: center;
  }
  .label--sleep { --bg: var(--sleep-bg); --ink: var(--sleep-ink); --art: var(--sleep-art); }
  .label--stress { --bg: var(--stress-bg); --ink: var(--stress-ink); --art: var(--stress-art); }
  .label--muscle { --bg: var(--muscle-bg); --ink: var(--muscle-ink); --art: var(--muscle-art); }
  .category {
    font-size: 15px;
    letter-spacing: 0.04em;
    text-transform: uppercase;
  }
  .product-name {
    font-family: "Playfair Display", serif;
    font-weight: 800;
    font-size: 50px;
    line-height: 1.02;
    text-transform: uppercase;
    margin-top: 18px;
    letter-spacing: 0.01em;
  }
  .ingredient-art {
    width: 130px;
    height: 130px;
    border-radius: 50%;
    background: var(--art);
    margin-top: 36px;
  }
  .benefit {
    margin-top: 52px;
    display: flex;
    align-items: center;
    gap: 12px;
    font-size: 16px;
    font-weight: 600;
    line-height: 1.25;
    text-transform: uppercase;
  }
  .benefit-dot {
    width: 9px;
    height: 9px;
    border-radius: 50%;
    background: var(--ink);
    opacity: 0.7;
  }
  .rule {
    width: 232px;
    height: 2px;
    background: var(--ink);
    margin-top: 10px;
  }
  .scent {
    margin-top: 12px;
    font-size: 16px;
    text-transform: uppercase;
    letter-spacing: 0.02em;
  }
  .label--muscle .scent { font-weight: 600; }
</style>
</head>
<body>
  <section class="label label--sleep">
    <p class="category">Body Balm</p>
    <h2 class="product-name">Amber<br>Tide</h2>
    <div class="ingredient-art" role="img" aria-label="Line illustration of lavender sprigs with a small flower"></div>
    <p class="benefit"><span class="benefit-dot"></span><span>Naturally calm<br>mind &amp; body</span><span class="benefit-dot"></span></p>
    <div class="rule"></div>
    <p class="scent">Lavender + Vanilla</p>
  </section>

  <section class="label label--stress">
    <p class="category">Body Balm</p>
    <h2 class="product-name">Velvet<br>Arc</h2>
    <div class="ingredient-art" role="img" aria-label="Line illustration of a halved bergamot citrus fruit"></div>
    <p class="benefit"><span class="benefit-dot"></span><span>Naturally eases<br>tension &amp; anxiety</span><span class="benefit-dot"></span></p>
    <div class="rule"></div>
    <p class="scent">Bergamot + Cedarwood</p>
  </section>

  <section class="label label--muscle">
    <p class="category">Body Balm</p>
    <h2 class="product-name">Copper<br>Harbor</h2>
    <div class="ingredient-art" role="img" aria-label="Line illustration of mint leaves"></div>
    <p class="benefit"><span class="benefit-dot"></span><span>Naturally smooth<br>achy muscles</span><span class="benefit-dot"></span></p>
    <div class="rule"></div>
    <p class="scent">Eucalyptus + Mint</p>
  </section>
</body>
</html>
```